Business Card for Business consulting practice

Need a design for a consultant business card. Simple and elegant.
I need the following information on the card:
Logo: (see uploaded file)
Company name: Callendry Advisory Group
Name: Noel Fardwick
Title: Managing Director - Aerospace and Defence
Phone #: 438-261-7083
e-mail: noel.fardwick@callendry.example
Website: www.callendry.example
Tagline: Proposals Management and Capture support for complex procurements

```html
<!DOCTYPE html>
<html lang="en">
<head>
<meta charset="utf-8">
<title>Callendry Advisory Group – Business Card</title>
<link href="https://fonts.googleapis.com/css2?family=Cinzel:wght@500&family=Montserrat:wght@400;500&family=Arimo:wght@400;700&display=swap" rel="stylesheet">
<style>
  :root {
    --navy: #0c2b44;
    --blue: #1592c0;
    --white: #ffffff;
    --paper: #e9eaec;
  }
  * { box-sizing: border-box; margin: 0; padding: 0; }
  html, body { width: 1200px; height: 802px; overflow: hidden; background: var(--paper); }
  .stage { position: relative; width: 1200px; height: 802px; }
  .card {
    position: absolute; top: 251px; width: 520px; height: 300px;
    background: var(--navy); overflow: hidden;
    box-shadow: 0 6px 18px rgba(0,0,0,.18);
  }
  .card--front { left: 50px; }
  .card--back { left: 630px; }

  .front-panel { position: absolute; inset: 0; }
  .front-mark {
    position: absolute; right: 34px; top: 70px; width: 170px;
    display: flex; align-items: center; gap: 10px;
    font-family: "Cinzel", serif; font-weight: 500; font-size: 24px; color: var(--navy);
  }
  .front-mark .dot { width: 16px; height: 16px; border-radius: 50%; background: var(--blue); flex: none; }

  .wordmark { font-family: "Cinzel", serif; font-weight: 500; color: var(--white); letter-spacing: 1px; line-height: 1; }
  .subline {
    display: flex; align-items: center; gap: 8px;
    font-family: "Montserrat", sans-serif; font-weight: 400; color: var(--blue);
    text-transform: uppercase;
  }
  .subline::before, .subline::after { content: ""; height: 1px; background: var(--blue); flex: 1; }

  .front-brand { position: absolute; left: 30px; top: 40px; width: 230px; }
  .front-brand .wordmark { font-size: 30px; }
  .front-brand .subline { font-size: 8px; letter-spacing: 3px; margin-top: 6px; }

  .person { position: absolute; left: 30px; top: 118px; font-family: "Arimo", sans-serif; }
  .person-name { color: var(--blue); font-weight: 700; font-size: 20px; text-transform: uppercase; }
  .person-role { color: var(--white); font-size: 12.5px; line-height: 1.35; margin-top: 3px; }

  .contact { position: absolute; left: 30px; top: 200px; list-style: none; font-family: "Arimo", sans-serif; }
  .contact li { display: flex; align-items: center; gap: 9px; color: var(--white); font-size: 12.5px; line-height: 1; margin-bottom: 8px; }
  .contact svg { width: 12px; height: 12px; flex: none; }

  .back-brand { position: absolute; left: 0; right: 0; top: 88px; text-align: center; }
  .back-brand .wordmark { font-size: 44px; }
  .back-brand .subline { width: 340px; margin: 8px auto 0; font-size: 11px; letter-spacing: 5px; }
  .tagline {
    position: absolute; left: 0; right: 0; top: 196px; text-align: center;
    font-family: "Arimo", sans-serif; font-size: 13px; line-height: 1.45; color: var(--white);
  }
</style>
</head>
<body>
<main class="stage">

  <section class="card card--front" aria-label="Business card front">
    <svg class="front-panel" viewBox="0 0 520 300" aria-hidden="true">
      <polygon points="300,0 520,0 520,300 420,300" fill="var(--white)"/>
    </svg>
    <div class="front-mark"><span class="dot"></span>Callendry</div>

    <div class="front-brand">
      <div class="wordmark">CALLENDRY</div>
      <div class="subline">Advisory Group</div>
    </div>

    <div class="person">
      <div class="person-name">Noel Fardwick</div>
      <div class="person-role">Managing Director<br>Aerospace and Defence</div>
    </div>

    <ul class="contact">
      <li>
        <svg viewBox="0 0 12 12"><path d="M2.5 1 4.5 3 3.6 4.6a7 7 0 0 0 3.8 3.8L9 7.5l2 2-1.4 1.5C5.5 10.8 1.2 6.5 1 2.4Z" fill="var(--blue)"/></svg>
        438-261-7083
      </li>
      <li>
        <svg viewBox="0 0 12 12"><rect x="0.5" y="2" width="11" height="8" fill="var(--blue)"/><path d="M0.5 2 6 6.5 11.5 2" stroke="var(--navy)" fill="none"/></svg>
        noel.fardwick@callendry.example
      </li>
      <li>
        <svg viewBox="0 0 12 12"><circle cx="6" cy="6" r="5.5" fill="var(--blue)"/><path d="M0.5 6h11M6 .5c-3 3.5-3 7.5 0 11M6 .5c3 3.5 3 7.5 0 11" stroke="var(--navy)" stroke-width=".8" fill="none"/></svg>
        www.callendry.example
      </li>
    </ul>
  </section>

  <section class="card card--back" aria-label="Business card back">
    <div class="back-brand">
      <div class="wordmark">CALLENDRY</div>
      <div class="subline">Advisory Group</div>
    </div>
    <p class="tagline">Proposals Management And<br>Capture Support For Complex Procurements</p>
  </section>

</main>
</body>
</html>
```